Customs House descriptive business cards

We require a two-sided business card that has a simple yet elegant design. We want to be able to promote our services as a customs house. This card should include our logo, contact info and services offered with the logo being on one side and the contact info and services on the flip side

Target Market(s)

Importers / exporters to and from the Bahamas

Industry/Entity Type

Logistics

Contact Information for Business Card

The front side of the card could have the logo and the flip side should have the other relevant info

Font styles to use
Serif

Colors

Designer to choose colors to be used in the design.

Requirements
Must have
• (Harbourline Agents Ltd) Logo, address and contact info also services:
• import customs clearance, Delivery & HAndling services,Florida pickups, Export packing & Crating Services, export customs clearance, Consulting

```html
<!DOCTYPE html>
<html lang="en">
<head>
<meta charset="utf-8">
<title>Harbourline Agents Ltd – Business Card</title>
<link rel="stylesheet" href="https://fonts.googleapis.com/css2?family=Cinzel:wght@700&family=Lato:wght@400;700&display=swap">
<style>
  :root {
    --bg: #e6e7e9;
    --brand-blue: #1f8fd6;
    --brand-blue-dark: #1778c2;
    --brand-blue-light: #2ba0e0;
    --ink: #2a2a2a;
    --paper: #ffffff;
    --icon: #1a7cc4;
  }
  * { box-sizing: border-box; margin: 0; padding: 0; }
  html, body { width: 1200px; height: 900px; overflow: hidden; }
  body {
    background: var(--bg);
    font-family: "Lato", Arial, sans-serif;
    color: var(--ink);
    position: relative;
  }
  .card {
    position: absolute;
    width: 560px;
    height: 320px;
    border-radius: 26px;
    overflow: hidden;
  }
  .card-front {
    left: 60px; top: 110px;
    background: linear-gradient(160deg, var(--brand-blue-dark), var(--brand-blue-light));
    display: flex; align-items: center; justify-content: center;
  }
  .wordmark {
    font-family: "Cinzel", Georgia, serif;
    font-weight: 700;
    text-align: center;
    line-height: 1.15;
  }
  .card-front .wordmark { color: var(--paper); font-size: 34px; }
  .card-front .wordmark-mark {
    width: 22px; height: 22px; border-radius: 50%;
    background: var(--paper); margin: 0 auto 14px;
  }
  .card-back {
    left: 580px; top: 470px;
    background: var(--paper);
    padding: 34px 26px 0 36px;
    display: grid;
    grid-template-columns: 220px 1fr;
    column-gap: 28px;
  }
  .card-back::after {
    content: "";
    position: absolute;
    left: 0; right: 0; bottom: 0;
    height: 12px;
    background: var(--brand-blue);
  }
  .card-back .wordmark {
    color: var(--brand-blue);
    font-size: 21px;
    text-align: left;
    display: flex; align-items: center; gap: 10px;
  }
  .card-back .wordmark-mark {
    width: 14px; height: 14px; background: var(--brand-blue); flex: none;
  }
  .person { margin-top: 30px; }
  .person-name {
    font-family: "Cinzel", Georgia, serif; font-weight: 700;
    color: var(--brand-blue); font-size: 19px;
  }
  .person-title { font-size: 15px; margin-bottom: 4px; }
  .contact { list-style: none; font-size: 15px; line-height: 1.45; }
  .contact li { display: flex; align-items: center; gap: 7px; }
  .contact svg { width: 12px; height: 12px; fill: var(--icon); flex: none; }
  .address { font-size: 15px; line-height: 1.35; margin-top: 2px; }
  .services {
    list-style: none; font-size: 15px; line-height: 1.55;
    margin-top: 74px;
  }
  .services li { display: flex; align-items: center; gap: 7px; white-space: nowrap; }
  .services svg { width: 12px; height: 12px; flex: none; }
  .services path { fill: none; stroke: var(--brand-blue); stroke-width: 2; }
</style>
</head>
<body>
  <section class="card card-front" aria-label="Card front">
    <div class="wordmark">
      <div class="wordmark-mark"></div>
      Harbourline<br>Agents Ltd
    </div>
  </section>

  <section class="card card-back" aria-label="Card back">
    <div class="identity">
      <div class="wordmark"><span class="wordmark-mark"></span>Harbourline<br>Agents Ltd</div>
      <div class="person">
        <div class="person-name">DANIEL ROWE</div>
        <div class="person-title">Managing Director</div>
        <ul class="contact">
          <li><svg viewBox="0 0 12 12"><path d="M2 1h3l1 3-1.5 1a6 6 0 0 0 2.5 2.5L8 6l3 1v3a1 1 0 0 1-1 1A9 9 0 0 1 1 2a1 1 0 0 1 1-1z"/></svg>044-210 387 654</li>
          <li><svg viewBox="0 0 12 12"><path d="M0 2h12v8H0z"/></svg>hello@harbourline.com</li>
          <li><svg viewBox="0 0 12 12"><circle cx="6" cy="6" r="6"/></svg>www.harbourline.com</li>
        </ul>
        <p class="address">18 Marina Quay, Unit 4<br>Nassau, Bahamas 20417</p>
      </div>
    </div>
    <ul class="services">
      <li><svg viewBox="0 0 12 12"><path d="M1.5 6.5l3 3 6-7"/></svg>Import customs clearance</li>
      <li><svg viewBox="0 0 12 12"><path d="M1.5 6.5l3 3 6-7"/></svg>Delivery &amp; HAndling services</li>
      <li><svg viewBox="0 0 12 12"><path d="M1.5 6.5l3 3 6-7"/></svg>Florida pickups</li>
      <li><svg viewBox="0 0 12 12"><path d="M1.5 6.5l3 3 6-7"/></svg>Export packing &amp; Crating Services</li>
      <li><svg viewBox="0 0 12 12"><path d="M1.5 6.5l3 3 6-7"/></svg>Export customs clearance</li>
      <li><svg viewBox="0 0 12 12"><path d="M1.5 6.5l3 3 6-7"/></svg>Consulting</li>
    </ul>
  </section>
</body>
</html>
```